Product Page

We're marketing an on line educational product, and need a savvy designer to fix a web page that lacks pazazz. We're looking for a designer who can take a lot of information and present it neatly and elegantly, and put all the relevant testimonials in there without loosing cool factor. Right now we need just one page designed, but the winner will have the chance to re-do the entire site, with lots more content coming down the line that will need the new look.

The current page is here: www.plorvetune.com/sign-up. This should be combined with the attached PDF that has a lot more text information.

Note: The previous file listed as a pdf was a jpg. Sorry about that! Now there's a real pdf available for you to download.

I have added a jpg of myself. If you can use that I would appreciate it. I've also uploaded an example of a pricing page. Let me know how you would charge for this extra page.

Target Market(s)

Men and women in their forties who want to improve their singing but have other careers and are looking for high quality voice instruction.

The page must have an attractive "Get Started" button prominently displayed.

Industry/Entity Type

Marketing

Requirements
Must have
• Above the fold: clear buy now button, some testimonials, and the video. Should have a background that makes reading the text easy-not black. The new page must work somehow with the existing theme, although we will be re-designing the whole site soon with your help.
Nice to have
• Some navigation to organize a lot of text

```html
<!DOCTYPE html>
<html lang="en">
<head>
<meta charset="utf-8">
<title>Evan Marlow School of Voice</title>
<link rel="stylesheet" href="https://fonts.googleapis.com/css2?family=Oswald:wght@300;400;600&family=Arimo:wght@400&display=swap">
<style>
  :root {
    --nav-bg: #474747;
    --page-bg: #e6e6e4;
    --panel: #262626;
    --accent: #29a8e0;
    --nav-text: #f2f2f2;
    --head-text: #bdbdbd;
    --body-text: #cfcfcf;
    --muted: #a5a5a5;
    --footer: #000000;
    --divider: #6a6a6a;
    --player: #1a1a1a;
    --photo-top: #3a3a3a;
    --photo-bottom: #050505;
  }
  * { box-sizing: border-box; margin: 0; padding: 0; }
  html, body { width: 1200px; height: 1200px; overflow: hidden; }
  body { position: relative; background: var(--page-bg); font-family: "Arimo", Arial, sans-serif; }

  .main-nav { position: absolute; left: 0; top: 0; width: 1200px; height: 92px; background: var(--nav-bg); }
  .main-nav a { position: absolute; top: 28px; font-family: "Oswald", sans-serif; font-weight: 300; font-size: 29px; line-height: 1; color: var(--nav-text); text-decoration: none; letter-spacing: -0.3px; }
  .main-nav a.is-current { color: var(--accent); }

  .coach-photo { position: absolute; left: 0; top: 92px; width: 300px; height: 945px; background: linear-gradient(180deg, var(--photo-top) 0%, #151515 45%, var(--photo-bottom) 100%); }

  .brand { position: absolute; left: 372px; top: 152px; display: flex; align-items: center; gap: 16px; }
  .brand-dot { width: 56px; height: 56px; border-radius: 50%; background: var(--accent); }
  .brand-name { font-family: "Oswald", sans-serif; font-weight: 300; color: #333; line-height: 1.05; }
  .brand-name .line-1 { display: block; font-size: 42px; }
  .brand-name .line-2 { display: block; font-size: 20px; padding-left: 28px; }

  .get-started { position: absolute; left: 875px; top: 157px; width: 263px; height: 62px; background: var(--accent); border: 2px solid #fff; outline: 1px solid var(--accent); display: flex; align-items: center; justify-content: center; font-family: "Oswald", sans-serif; font-weight: 600; font-size: 40px; color: #fff; text-decoration: none; letter-spacing: -0.5px; }
  .discount { position: absolute; left: 874px; top: 226px; width: 264px; text-align: right; font-family: "Oswald", sans-serif; font-weight: 300; font-size: 26px; color: #555; white-space: nowrap; }
  .discount strong { font-weight: 300; color: var(--accent); }

  .content-panel { position: absolute; left: 243px; top: 287px; width: 896px; height: 689px; background: var(--panel); }

  .video { position: absolute; left: 16px; top: 22px; width: 440px; height: 287px; background: var(--player); }
  .video-frame { position: absolute; left: 0; top: 0; width: 440px; height: 251px; background: linear-gradient(180deg, #5a5a5a 0%, #444 60%, #2e2e33 100%); }
  .player-bar { position: absolute; left: 0; top: 251px; width: 440px; height: 36px; background: #111; border-top: 3px solid #000; }
  .player-bar .pause { position: absolute; left: 10px; top: 10px; }
  .player-bar .time { position: absolute; top: 11px; font-size: 9px; color: #666; }
  .player-bar .track { position: absolute; left: 76px; top: 6px; width: 236px; height: 24px; background: #333; }
  .player-bar .handle { position: absolute; left: 0; top: 0; width: 10px; height: 24px; background: var(--accent); }
  .player-bar .volume { position: absolute; left: 356px; top: 11px; }

  .intro { position: absolute; left: 19px; top: 324px; width: 430px; font-family: "Oswald", sans-serif; font-weight: 300; font-size: 27px; line-height: 34px; letter-spacing: -0.4px; color: var(--head-text); }
  .intro em { font-style: normal; color: var(--accent); }

  .guarantee { position: absolute; left: 37px; top: 452px; width: 380px; font-size: 13.5px; line-height: 17px; color: var(--muted); }
  .guarantee p { margin-bottom: 17px; }
  .guarantee .sign-off { font-size: 20px; margin-top: 24px; color: #8e8e8e; }

  .testimonial { position: absolute; left: 489px; width: 385px; }
  .testimonial p { font-size: 14px; line-height: 17.5px; color: var(--body-text); }
  .testimonial .author { position: relative; height: 90px; margin-top: 24px; }
  .testimonial .avatar { position: absolute; left: 1px; top: 0; width: 89px; height: 89px; border: 2px solid #fff; }
  .testimonial .name { position: absolute; left: 105px; top: 38px; font-family: "Oswald", sans-serif; font-weight: 300; font-size: 30px; line-height: 1; color: var(--head-text); }
  .testimonial .place { position: absolute; left: 105px; top: 72px; font-size: 14px; color: var(--body-text); }
  .testimonial-one { top: 27px; }
  .testimonial-two { top: 334px; }
  .testimonial-divider { position: absolute; left: 490px; top: 307px; width: 380px; height: 1px; background: var(--divider); }

  .site-footer { position: absolute; left: 0; top: 1037px; width: 1200px; height: 163px; background: var(--footer); }
  .footer-brand { position: absolute; left: 52px; top: 40px; display: flex; align-items: center; gap: 14px; }
  .footer-brand .brand-dot { width: 50px; height: 50px; }
  .footer-brand .brand-name { color: #fff; }
  .footer-brand .line-1 { font-size: 38px; }
  .footer-brand .line-2 { font-size: 19px; padding-left: 24px; }
  .footer-links { position: absolute; left: 397px; top: 66px; display: flex; gap: 17px; font-size: 14px; }
  .footer-links a { color: var(--accent); text-decoration: none; }
  .copyright { position: absolute; left: 397px; top: 96px; font-size: 13px; color: #eee; }
  .social { position: absolute; top: 57px; width: 50px; height: 50px; border-radius: 50%; }
  .social-one { left: 1009px; background: var(--accent); }
  .social-two { left: 1073px; background: #3b5a9a; }
</style>
</head>
<body>

<nav class="main-nav">
  <a class="is-current" style="left:36px" href="#">HOME</a>
  <a style="left:142px" href="#">VOICE LESSONS</a>
  <a style="left:346px" href="#">BLOG</a>
  <a style="left:448px" href="#">WHAT STUDENTS SAY</a>
  <a style="left:703px" href="#">THE INSTRUCTORS</a>
  <a style="left:935px" href="#">VOCAL ASCENT</a>
</nav>

<div class="coach-photo" role="img" aria-label="Black and white photo of the vocal coach, smiling, in a dark sweater"></div>

<div class="brand">
  <span class="brand-dot"></span>
  <span class="brand-name"><span class="line-1">Evan Marlow</span><span class="line-2">School of Voice</span></span>
</div>

<a class="get-started" href="#">GET STARTED</a>
<div class="discount"><strong>30% Discount</strong> Use Code: VA414</div>

<main class="content-panel">
  <div class="video">
    <div class="video-frame" role="img" aria-label="Video still of the coach speaking to camera with a name caption"></div>
    <div class="player-bar">
      <svg class="pause" width="10" height="14" viewBox="0 0 10 14"><rect x="0" y="0" width="3" height="14" fill="#29a8e0"/><rect x="6" y="0" width="3" height="14" fill="#29a8e0"/></svg>
      <span class="time" style="left:36px">00:09</span>
      <div class="track"><span class="handle"></span></div>
      <span class="time" style="left:320px">04:17</span>
      <svg class="volume" width="76" height="14" viewBox="0 0 76 14">
        <path d="M0 4 H3 L7 0 V14 L3 10 H0 Z" fill="#29a8e0"/>
        <g fill="#29a8e0"><rect x="11" y="2" width="2" height="10"/><rect x="15" y="2" width="2" height="10"/><rect x="19" y="2" width="2" height="10"/><rect x="23" y="2" width="2" height="10"/><rect x="27" y="2" width="2" height="10"/><rect x="31" y="2" width="2" height="10"/><rect x="35" y="2" width="2" height="10"/><rect x="39" y="2" width="2" height="10"/><rect x="43" y="2" width="2" height="10"/></g>
        <rect x="56" y="1" width="20" height="12" rx="3" fill="none" stroke="#29a8e0" stroke-width="2"/>
        <rect x="59" y="4" width="14" height="6" rx="1" fill="#29a8e0"/>
      </svg>
    </div>
  </div>

  <p class="intro">Professional vocal coach, <em>Evan D. Marlow</em> has laid the vocal foundation for thousands of singers worldwide, for 20+ years.</p>

  <div class="guarantee">
    <p>“I believe in Vocal Ascent wholeheartedly, and I want you to be fully satisfied with the program.</p>
    <p>That's why I stand behind Vocal Ascent with a 100% money-back guarantee.</p>
    <p>I am confident that by making this small investment now, you will learn the keys to achieving having a breakthrough with your voice.”</p>
    <p class="sign-off">Evan Marlow</p>
  </div>

  <article class="testimonial testimonial-one">
    <p>I have found through the years that the one method I can count on is Vocal Ascent. Evan Marlow has put together the fool proof method for training a voice that is dependable and authentic as you grow through your vocal practice. I recently joined a band with a harder rock sound than I had been used to. I worked through Vocal Ascent front to back, and now I am killing it on songs I had previously only dreamed about....</p>
    <div class="author">
      <div class="avatar" role="img" aria-label="Portrait photo of the student" style="background:linear-gradient(160deg,#6b6b6b,#1e1e1e)"></div>
      <span class="name">Dara Holt</span>
      <span class="place">San Francisco</span>
    </div>
  </article>

  <div class="testimonial-divider"></div>

  <article class="testimonial testimonial-two">
    <p>Since starting the program, my singing progress has been described as phenomenal, 400% improvement. My teachers have worked with people such as Dame Ilse Varrow, and they are impressed with my voice. I still feel I have progress to make, but mainly in areas of classical style. The raw instrument is there now....</p>
    <div class="author">
      <div class="avatar" role="img" aria-label="Portrait photo of the student" style="background:linear-gradient(160deg,#8a7a5e,#3a3226)"></div>
      <span class="name">Owen Tally</span>
      <span class="place">Australia</span>
    </div>
  </article>
</main>

<footer class="site-footer">
  <div class="footer-brand">
    <span class="brand-dot"></span>
    <span class="brand-name"><span class="line-1">Evan Marlow</span><span class="line-2">School of Voice</span></span>
  </div>
  <nav class="footer-links">
    <a href="#">Home</a><a href="#">About us</a><a href="#">Support</a><a href="#">EMMethod</a><a href="#">Privacy Policy</a><a href="#">Terms of use</a><a href="#">Sitemap</a>
  </nav>
  <p class="copyright">© Copyright 2009. Plorvetune.com. All Rights Reserved.</p>
  <a class="social social-one" href="#" aria-label="Social profile"></a>
  <a class="social social-two" href="#" aria-label="Social page"></a>
</footer>

</body>
</html>
```